Outdoor mass notification company needing business card design.

Our company name is Harrowgate Signal Systems Inc located in Amory Mississippi and we sell and maintain "Brantor" Mass Notification Sirens in the US. Outdoor sirens notify people of certain severe dangers such as tornados, severe thunderstorms, flooding, hurricanes and tsunamis. We also serve the oil and gas refining industries to warn of Chemical releases, fires, and lightning alerts.

Contact Information for Business Card

Name, title, cell number, email address

Requirements
Nice to have
• The Brantor logo and also the Mildvane logo.

```html
<!DOCTYPE html>
<html lang="en">
<head>
<meta charset="UTF-8">
<title>Harrowgate Signal Systems – Business Card</title>
<link href="https://fonts.googleapis.com/css2?family=Cinzel:wght@600&family=Montserrat:wght@400;700&display=swap" rel="stylesheet">
<style>
  :root {
    --backdrop: #2b2c30;
    --card-blue: #3a5a78;
    --navy: #2f4f6e;
    --ink: #2e3440;
    --paper: #ffffff;
    --faint-grey: #ececec;
  }
  * { box-sizing: border-box; margin: 0; padding: 0; }
  html, body { width: 1200px; height: 900px; overflow: hidden; }
  body {
    background: var(--backdrop);
    position: relative;
    font-family: "Montserrat", sans-serif;
  }
  .card {
    position: absolute;
    width: 580px;
    height: 330px;
    border-radius: 22px;
    overflow: hidden;
  }
  /* Front face */
  .card--front {
    left: 70px; top: 80px;
    background: var(--card-blue);
    display: flex; align-items: center; justify-content: center;
  }
  .front-brand {
    display: flex; align-items: center; gap: 22px;
  }
  .front-brand__dot {
    width: 30px; height: 30px; border-radius: 50%;
    background: var(--paper);
  }
  .front-brand__name {
    font-family: "Cinzel", serif;
    font-weight: 600;
    color: var(--paper);
    line-height: 1.05;
    font-size: 40px;
    letter-spacing: 1px;
  }
  .front-brand__name span { display: block; }
  .front-brand__name .line-two { font-size: 33px; }

  /* Back face */
  .card--back {
    left: 550px; top: 490px;
    background: var(--paper);
  }
  .back-decor {
    position: absolute;
    right: -60px; top: -70px;
    width: 300px; height: 300px;
    border-radius: 50%;
    background: var(--faint-grey);
  }
  .back-content {
    position: absolute;
    left: 44px; top: 34px;
  }
  .back-brand {
    font-family: "Cinzel", serif;
    font-weight: 600;
    color: var(--navy);
    font-size: 21px;
    line-height: 1.05;
  }
  .back-brand span { display: block; }
  .person { margin-top: 30px; position: relative; }
  .person__accent {
    position: absolute;
    left: -44px; top: 4px;
    width: 12px; height: 48px;
    background: var(--navy);
  }
  .person__name {
    font-weight: 700; color: var(--navy); font-size: 24px;
  }
  .person__title {
    font-size: 14px; color: var(--ink); margin-top: 2px;
  }
  .address {
    margin-top: 20px; font-size: 13px; color: var(--ink); line-height: 1.35;
  }
  .contacts { margin-top: 16px; list-style: none; }
  .contacts li {
    display: flex; align-items: center; gap: 10px;
    font-size: 13px; color: var(--ink); line-height: 1.6;
  }
  .contacts svg { width: 13px; height: 13px; fill: var(--navy); flex: none; }
</style>
</head>
<body>
  <section class="card card--front" aria-label="Business card front">
    <div class="front-brand">
      <div class="front-brand__dot"></div>
      <h1 class="front-brand__name">
        <span>Harrowgate</span>
        <span class="line-two">Signal Systems</span>
      </h1>
    </div>
  </section>

  <section class="card card--back" aria-label="Business card back">
    <div class="back-decor"></div>
    <div class="back-content">
      <h2 class="back-brand">
        <span>Harrowgate</span>
        <span>Signal Systems</span>
      </h2>
      <div class="person">
        <div class="person__accent"></div>
        <p class="person__name">Dale Merriton</p>
        <p class="person__title">CEO</p>
      </div>
      <p class="address">418 Canal Row, #12<br>Amory, MS 38821</p>
      <ul class="contacts">
        <li>
          <svg viewBox="0 0 16 16" aria-hidden="true"><path d="M3.5 1.5l2.5 0 1 3.5-1.6 1.2a9 9 0 0 0 4.4 4.4L11 9l3.5 1v2.5c0 1-1 2-2 2C6.5 14.5 1.5 9.5 1.5 3.5c0-1 1-2 2-2z"/></svg>
          662 555-0147
        </li>
        <li>
          <svg viewBox="0 0 16 16" aria-hidden="true"><path d="M1 3h14v10H1z M1.8 3.6L8 8.6l6.2-5H1.8z" fill-rule="evenodd"/></svg>
          info@harrowgatesignal.com
        </li>
        <li>
          <svg viewBox="0 0 16 16" aria-hidden="true"><circle cx="8" cy="8" r="7"/><path d="M1.5 8h13M8 1c-2.5 3-2.5 11 0 14M8 1c2.5 3 2.5 11 0 14" stroke="#fff" stroke-width="1" fill="none"/></svg>
          www.harrowgatesignal.com
        </li>
      </ul>
    </div>
  </section>
</body>
</html>
```